Dog grooming business card
This is a business card for m dog grooming business like it say above.
In the priorities box below I will have the text that I want on the card.

Industry/Entity Type

Business

Colors

Designer to choose colors to be used in the design.

Requirements
Must have
• My logo and the insurance stamp must be on the card.

Text it must have :

Professional grooming services
Email: lunabrisk@mailvane.net
Text or call 1 705 318 6642
TKV certified/member
Pet first aid certified
Next appointment ___________________________________
Nice to have
• Greens to match my logo

```html
<!DOCTYPE html>
<html lang="en">
<head>
<meta charset="utf-8">
<title>Luna Brisk – Grooming Business Card</title>
<link rel="stylesheet" href="https://fonts.googleapis.com/css2?family=Quattrocento:wght@400;700&family=Poiret+One&family=Open+Sans:wght@700;800&display=swap">
<style>
  :root {
    --leaf: #9dc43a;
    --leaf-text: #8fbf3a;
    --leaf-line: #8cbd33;
    --ink: #111111;
    --paper: #ffffff;
    --stage-top: #ffffff;
    --stage-bottom: #d3e39c;
    --badge-blue: #2a6db5;
    --card-edge: #7a7a7a;
  }
  * { margin: 0; padding: 0; box-sizing: border-box; }
  html, body { width: 1200px; height: 1000px; overflow: hidden; }
  body {
    position: relative;
    background: linear-gradient(180deg, var(--stage-top) 0%, var(--stage-bottom) 100%);
    font-family: "Quattrocento", Georgia, serif;
  }
  .card {
    position: absolute;
    left: 245px;
    width: 712px;
    height: 406px;
    overflow: hidden;
    border: 1px solid var(--card-edge);
  }
  .card-front { top: 27px; background: var(--paper); }
  .card-back { top: 523px; background: var(--leaf); }
  .card-art { position: absolute; inset: 0; width: 712px; height: 406px; display: block; }

  .brand-name {
    position: absolute;
    left: 0; right: 0;
    top: 96px;
    text-align: center;
    font-family: "Quattrocento", Georgia, serif;
    font-weight: 700;
    font-size: 30px;
    color: var(--leaf-text);
  }
  .tagline {
    position: absolute;
    left: 0; right: 0;
    top: 180px;
    text-align: center;
    font-size: 35px;
    letter-spacing: 2px;
    color: var(--leaf-text);
  }
  .contact {
    position: absolute;
    left: 0; right: 0;
    text-align: center;
    font-size: 26px;
  }
  .contact-email { top: 248px; }
  .contact-phone { top: 290px; }
  .contact-label { font-weight: 700; font-size: 23px; color: var(--leaf-text); }
  .contact-value { font-family: "Poiret One", "Century Gothic", sans-serif; font-weight: 700; color: var(--ink); }
  .credential {
    position: absolute;
    top: 356px;
    font-family: "Poiret One", "Century Gothic", sans-serif;
    font-weight: 700;
    font-size: 22px;
    color: var(--ink);
  }
  .credential-member { left: 87px; }
  .credential-firstaid { left: 420px; }

  .appointment-title {
    position: absolute;
    left: 0; right: 0;
    top: 26px;
    text-align: center;
    font-family: "Open Sans", Arial, sans-serif;
    font-weight: 800;
    font-size: 23px;
    color: var(--paper);
    text-shadow: 2px 2px 3px rgba(0,0,0,0.55);
  }
  .day-label, .field-label {
    font-family: "Open Sans", Arial, sans-serif;
    font-weight: 700;
    font-size: 14px;
    fill: #222;
  }
</style>
</head>
<body>

<section class="card card-front" aria-label="Business card front">
  <svg class="card-art" viewBox="0 0 712 406" aria-hidden="true">
    <path class="top-band" d="M0,0 H712 V166 Q356,100 0,166 Z" fill="var(--ink)"/>
    <path class="bottom-band" d="M0,310 Q356,386 712,310 V406 H0 Z" fill="var(--leaf)"/>
    <circle class="brand-dot" cx="356" cy="52" r="34" fill="var(--leaf)"/>
  </svg>
  <div class="brand-name">Luna Brisk</div>
  <h1 class="tagline" style="font-weight:400">Professional Grooming Services</h1>
  <p class="contact contact-email"><span class="contact-label">Email:</span> <span class="contact-value">lunabrisk@mailvane.net</span></p>
  <p class="contact contact-phone"><span class="contact-label">Text or call:</span> <span class="contact-value">1 705 318 6642</span></p>
  <p class="credential credential-member">TKV certified/member</p>
  <p class="credential credential-firstaid">Pet first aid certified</p>
</section>

<section class="card card-back" aria-label="Business card back">
  <svg class="card-art" viewBox="0 0 712 406">
    <rect class="pattern-field" x="0" y="0" width="712" height="406" fill="var(--leaf)" role="img" aria-label="Repeating pattern of small poodle motifs across the green background"/>
    <circle class="date-panel" cx="355" cy="227" r="166" fill="var(--paper)"/>
    <g class="day-picker">
      <circle cx="206" cy="94" r="25" fill="var(--paper)"/>
      <circle cx="162" cy="157" r="25" fill="var(--paper)"/>
      <circle cx="151" cy="226" r="25" fill="var(--paper)"/>
      <circle cx="162" cy="290" r="25" fill="var(--paper)"/>
      <circle cx="196" cy="354" r="25" fill="var(--paper)"/>
      <text class="day-label" x="206" y="99" text-anchor="middle">MON</text>
      <text class="day-label" x="162" y="162" text-anchor="middle">TUE</text>
      <text class="day-label" x="151" y="231" text-anchor="middle">WED</text>
      <text class="day-label" x="162" y="295" text-anchor="middle">THU</text>
      <text class="day-label" x="196" y="359" text-anchor="middle">FRI</text>
    </g>
    <line class="date-line" x1="240" y1="168" x2="450" y2="168" stroke="var(--leaf-line)" stroke-width="2"/>
    <text class="field-label" x="212" y="245">AT</text>
    <line class="time-line" x1="240" y1="245" x2="471" y2="245" stroke="var(--leaf-line)" stroke-width="2"/>
    <text class="field-label" x="389" y="235">AM</text>
    <text class="field-label" x="444" y="235">PM</text>
    <rect class="insurance-badge" x="252" y="280" width="188" height="84" rx="12" fill="var(--paper)" stroke="var(--badge-blue)" stroke-width="1.5"/>
    <circle class="brand-medallion" cx="567" cy="202" r="70" fill="var(--leaf)" stroke="var(--paper)" stroke-width="5"/>
  </svg>
  <h2 class="appointment-title">YOUR NEXT APPOINTMENT IS ON:</h2>
</section>

</body>
</html>
```